Wholesale in Gold Jewellery & Gold Bullion

We are an established gold jewellery and gold bullion wholesaler selling these products to international clients. We already have a name and logo of our company, hence please view attached current card design. We need a completely new design to compliment our business and industry and the final design should be new and elegant.

Contact Information for Business Card

New card details must be same as per current card. Like logo, name, tel no. & etc.

Colors

Designer to choose colors to be used in the design.

```html
<!DOCTYPE html>
<html lang="en">
<head>
<meta charset="utf-8">
<title>Aurelian &amp; Co – Business Card</title>
<link href="https://fonts.googleapis.com/css2?family=Montserrat:wght@400;500;600&family=Tinos:wght@700&display=swap" rel="stylesheet">
<style>
  :root {
    --page-bg: #e9e6e1;
    --card-white: #f4f4f3;
    --gold: #e5a823;
    --charcoal-top: #3d4245;
    --charcoal-bottom: #212628;
    --ink-dark: #2b1d17;
    --text-light: #f2f2f2;
  }
  * { margin: 0; padding: 0; box-sizing: border-box; }
  html, body {
    width: 1200px;
    height: 900px;
    overflow: hidden;
    background: var(--page-bg);
  }
  .canvas {
    position: relative;
    width: 1200px;
    height: 900px;
  }
  .card {
    position: absolute;
    left: 100px;
    top: 164px;
    width: 1000px;
    height: 572px;
    background: var(--card-white);
    box-shadow: 0 10px 30px rgba(0,0,0,0.18);
    overflow: hidden;
  }
  .card-header {
    position: absolute;
    left: 0; top: 0;
    width: 100%;
    height: 245px;
    display: flex;
    align-items: center;
    justify-content: center;
    gap: 40px;
    padding-top: 6px;
  }
  .brand-dot {
    width: 72px;
    height: 72px;
    border-radius: 50%;
    background: var(--gold);
  }
  .brand-name {
    font-family: "Tinos", "Times New Roman", serif;
    font-weight: 700;
    font-size: 38px;
    letter-spacing: 0.5px;
    color: var(--ink-dark);
  }
  .gold-rule {
    position: absolute;
    left: 0; top: 245px;
    width: 100%;
    height: 12px;
    background: var(--gold);
  }
  .card-body {
    position: absolute;
    left: 0; top: 268px;
    width: 100%;
    height: 304px;
    background: linear-gradient(180deg, var(--charcoal-top), var(--charcoal-bottom));
    font-family: "Montserrat", Arial, sans-serif;
    color: var(--text-light);
  }
  .person {
    position: absolute;
    left: 95px;
    top: 40px;
  }
  .person-name {
    font-size: 34px;
    font-weight: 600;
    color: var(--gold);
    letter-spacing: 0.5px;
    line-height: 1.1;
  }
  .person-role {
    font-size: 26px;
    font-weight: 400;
    line-height: 1.2;
    margin-bottom: 14px;
  }
  .person-address {
    font-size: 20px;
    font-style: normal;
    line-height: 1.4;
  }
  .contacts {
    position: absolute;
    right: 55px;
    top: 100px;
    list-style: none;
  }
  .contact-item {
    display: flex;
    align-items: center;
    justify-content: flex-end;
    gap: 26px;
    height: 36px;
    font-size: 22px;
    letter-spacing: 0.3px;
  }
  .contact-icon {
    width: 26px;
    height: 26px;
    flex: none;
  }
</style>
</head>
<body>
<main class="canvas">
  <article class="card">
    <header class="card-header">
      <span class="brand-dot" aria-hidden="true"></span>
      <h1 class="brand-name">AURELIAN &amp; CO PTE LTD</h1>
    </header>
    <div class="gold-rule"></div>
    <section class="card-body">
      <div class="person">
        <p class="person-name">Ravin Solanki</p>
        <p class="person-role">Director</p>
        <address class="person-address">12 Kestrel Lane,<br>Singapore 208815</address>
      </div>
      <ul class="contacts">
        <li class="contact-item">
          <span>+65 9100 2468</span>
          <svg class="contact-icon" viewBox="0 0 26 26" aria-label="Mobile">
            <rect x="7" y="2" width="12" height="22" rx="2" fill="none" stroke="var(--gold)" stroke-width="2.2"/>
            <line x1="11" y1="20" x2="15" y2="20" stroke="var(--gold)" stroke-width="2"/>
          </svg>
        </li>
        <li class="contact-item">
          <span>+65 6200 1357</span>
          <svg class="contact-icon" viewBox="0 0 26 26" aria-label="Telephone">
            <path d="M8 3 L12 8 L9.5 11 C11 14.5 13 16.5 16 17.5 L18.5 15 L23 19 L20 23 C12 22 5 14 4 6 Z" fill="var(--gold)"/>
          </svg>
        </li>
        <li class="contact-item">
          <span>+65 6200 1358</span>
          <svg class="contact-icon" viewBox="0 0 26 26" aria-label="Fax">
            <rect x="7" y="2" width="12" height="8" fill="none" stroke="var(--gold)" stroke-width="2"/>
            <rect x="2" y="10" width="22" height="11" rx="2" fill="var(--gold)"/>
            <rect x="6" y="21" width="14" height="3" fill="var(--gold)"/>
          </svg>
        </li>
        <li class="contact-item">
          <span>ravin@aurelianco.com</span>
          <svg class="contact-icon" viewBox="0 0 26 26" aria-label="Email">
            <rect x="2" y="6" width="22" height="15" fill="var(--gold)"/>
            <polyline points="2,6 13,15 24,6" fill="none" stroke="var(--charcoal-bottom)" stroke-width="1.8"/>
          </svg>
        </li>
      </ul>
    </section>
  </article>
</main>
</body>
</html>
```